Very Simple Web Redesign Project - Using Photoshop

Required is a very simple website home page redesign for the following site: http://www.tallowcrestslate.com.au/
I require this as a Photoshop design.
The basic look and feel of the site needs to remain.
Specifically the colours don't need to be changed.
The positioning of the site is currently correct for the target market.
The site does not need to be made super slick looking. Just upgraded to a new version.
The current text can all be used.
The only menus necessary are a horizontal menu at the top, and a simple horizontal text menu at the bottom of the page. Do NOT retain the vertical menu on the home page (having the items "Our Gallery", "Our Services", "Enquire Now").
Give the horizontal menu the following items:
Home | Slate Roof Repairs | Slate Reroofing | Slate Roof Benefits | Other Services | Photo Gallery | FAQ's | Free Quote | Contact Us
The picture of the house at the top RHS of the page needs to be reduced in size by approx 50% and moved to the top LHS of the page.
Please place the following text into the top of the page:
"Call Now: 0427 618 392"
Keep the four pictures on the home page layout. Some larger images attached.
Thanks,
Rob
Updates
Hi,
Thanks for all the designs.
I am working with my client to get which one they like the most.
Thanks,
Rob

```html
<!DOCTYPE html>
<html lang="en">
<head>
<meta charset="utf-8">
<title>Tallowcrest Slate – Slate roof specialists</title>
<link href="https://fonts.googleapis.com/css2?family=Arimo:wght@400;700&display=swap" rel="stylesheet">
<style>
  :root{
    --forest:#345a1c;
    --forest-deep:#2c4d17;
    --leaf:#76a843;
    --panel:#f0f0f0;
    --ink:#2f5a14;
    --heading:#244a0f;
    --rule:#cfcfcf;
    --cloud:#8a9f7e;
    --cloud-light:#b4c0aa;
    --cloud-dark:#7d9470;
    --white:#ffffff;
  }
  *{margin:0;padding:0;box-sizing:border-box}
  html,body{width:1200px;height:866px;overflow:hidden}
  body{background:var(--forest);font-family:"Arimo",Arial,sans-serif;position:relative;color:var(--ink)}
  .top-band{position:absolute;left:0;top:0;width:1200px;height:213px;background:linear-gradient(var(--leaf),#6ea03c);border-top:8px solid var(--forest-deep)}
  .brand{position:absolute;left:170px;top:26px;display:flex;align-items:center;gap:12px}
  .brand-mark{width:58px;height:58px;background:var(--forest-deep)}
  .brand-name{font-size:38px;font-weight:700;color:var(--white);letter-spacing:-0.5px}
  .call{position:absolute;left:884px;top:34px;color:var(--white);line-height:1}
  .call-label{font-size:17px;display:block}
  .call-number{font-size:23px;display:block;margin-top:2px}
  .main-nav{position:absolute;left:259px;top:99px;display:flex;gap:17px;font-size:12.5px;color:var(--white)}
  .hero{position:absolute;left:145px;top:124px;width:910px;height:337px;border-top:3px solid #c9d6b8;box-shadow:0 5px 8px rgba(0,0,0,.35)}
  .hero-photo{position:absolute;left:0;top:0;width:612px;height:334px;background:linear-gradient(160deg,#5b7d3a 0%,#7b5560 35%,#8a6670 60%,#a9a07f 88%,#d9d3c3 100%)}
  .hero-panel{position:absolute;left:612px;top:0;width:298px;height:334px;background:linear-gradient(#1d4010,#2d5719)}
  .hero-panel h1{position:absolute;left:12px;top:27px;font-size:30px;font-weight:400;color:var(--white)}
  .hero-panel p{position:absolute;left:12px;top:68px;width:270px;font-size:11.5px;line-height:15.3px;color:var(--white)}
  .credentials{position:absolute;left:12px;top:202px;font-size:9px;color:var(--white);letter-spacing:.3px}
  .thumb{position:absolute;top:214px;height:120px}
  .thumb-a{left:12px;width:148px;background:linear-gradient(135deg,#8a4a3a,#6d7480 55%,#5a6470)}
  .thumb-b{left:160px;width:138px;background:linear-gradient(150deg,#4f6b3c,#7a6f6a 50%,#d8d6d0)}
  .content{position:absolute;left:145px;top:479px;width:910px;height:387px;background:var(--panel)}
  .col{position:absolute;top:20px;font-size:12px;line-height:13.8px}
  .col h2{font-size:14px;font-weight:700;color:var(--heading);margin-bottom:10px}
  .col p{margin-bottom:13.8px}
  .col-about{left:34px;width:270px}
  .col-services{left:332px;width:276px}
  .col-area{left:624px;width:276px}
  .divider{position:absolute;top:47px;width:1px;height:252px;background:var(--rule)}
  .services-list{list-style:none;margin-bottom:13.8px}
  .services-list li{position:relative;padding-left:10px}
  .services-list li::before{content:"";position:absolute;left:1px;top:4px;border-left:4px solid var(--ink);border-top:3px solid transparent;border-bottom:3px solid transparent}
  .read-more{font-weight:700;color:var(--heading)}
  .tag-cloud{position:absolute;left:624px;top:0;width:286px;height:300px;color:var(--cloud);font-weight:700;line-height:1}
  .tag-cloud span{position:absolute;white-space:nowrap}
  .tag-cloud .tag-s{font-size:12px}
  .tag-cloud .tag-m{font-size:16px;color:var(--cloud-dark)}
  .tag-cloud .tag-l{font-size:22px}
  .tag-cloud .tag-faint{color:var(--cloud-light)}
  .site-footer{position:absolute;left:34px;top:334px;width:843px;border-top:1px solid var(--ink);padding-top:6px;display:flex;justify-content:space-between;font-size:10px;letter-spacing:.4px}
  .footer-nav{display:flex;gap:9px}
</style>
</head>
<body>
  <header class="top-band">
    <div class="brand">
      <div class="brand-mark"></div>
      <div class="brand-name">Tallowcrest Slate</div>
    </div>
    <div class="call">
      <span class="call-label">Call for a quote</span>
      <span class="call-number">0427 618 392</span>
    </div>
    <nav class="main-nav">
      <span>Home</span><span>Slate Roof Repairs</span><span>Slate Reroofing</span><span>Slate Roof Benefits</span><span>Other Services</span><span>Photo Gallery</span><span>FAQs</span><span>Free Quote</span><span>Contact Us</span>
    </nav>
  </header>

  <section class="hero">
    <div class="hero-photo" role="img" aria-label="Conical slate roof with copper gutter among trees"></div>
    <div class="hero-panel">
      <h1>Slate roof specialists</h1>
      <p>At Tallowcrest Slate we specialize in the upkeep, maintenance, repair and replacement of all types of slate roof as well as wood shingles. We can track down the leak that just won't go away or give your house a complete re-roof. We can also provide all your guttering needs.</p>
      <div class="credentials">ABN 47 302 118 905 &nbsp; Lic. No. 204417C</div>
      <div class="thumb thumb-a" role="img" aria-label="Slate roof beside red brick wall with downpipe"></div>
      <div class="thumb thumb-b" role="img" aria-label="Re-roofed slate house with bay window"></div>
    </div>
  </section>

  <main class="content">
    <div class="divider" style="left:317px"></div>
    <div class="divider" style="left:612px"></div>

    <section class="col col-about">
      <h2>About Tallowcrest Slate</h2>
      <p>Tallowcrest Slate is a small company and as such we do not have the overheads that larger companies do. Quality work and attention to detail are our trademark.</p>
      <p>All photos on this web site consist of work which I have personally done. The above photos provide at a quick glance a reasonable cross section of the type of work I do.</p>
      <p>By clicking on the photo gallery link you can see other work including some before and after shots.</p>
      <p>Feel free to call at your earliest convenience to organise an obligation-free quote or click on the contact us link and send us an e-mail.</p>
    </section>

    <section class="col col-services">
      <h2>Our Services</h2>
      <p>At Tallowcrest Slate we provide a variety of services in the upkeep, maintenance and or replacement of your slate and wood shingle roof.</p>
      <ul class="services-list">
        <li>tracking down and handling leaks</li>
        <li>replacement of broken slate</li>
        <li>re-securing slipped slate</li>
        <li>replacement of roofing valleys</li>
        <li>replacement and or maintenance of all types of ridge capping</li>
        <li>gutter, downpipe and gutter guard installation and replacement</li>
        <li>re-nailing of slate</li>
        <li>re-roofing in new or second hand slate</li>
      </ul>
      <p>We are also able to handle all your wood roofing shingle requirements. <span class="read-more">Read more</span>...</p>
    </section>

    <section class="col col-area">
      <h2>Sydney Service Area</h2>
      <p>We service all inner city suburbs of Sydney roughly covering an area encompassing Gordon to Epping, Mosman to Bondi, Coogee to Kogarah and Kingsgrove to Burwood and Concord.</p>
    </section>

    <div class="tag-cloud">
      <span class="tag-s" style="left:12px;top:118px">Roof Restoration</span>
      <span class="tag-l" style="left:70px;top:130px">Slate</span>
      <span class="tag-s" style="left:131px;top:130px">Wood Shingles</span>
      <span class="tag-l tag-faint" style="left:29px;top:153px">Roof Tiles</span>
      <span class="tag-m" style="left:154px;top:160px">Ridge Capping</span>
      <span class="tag-s" style="left:5px;top:178px">Guttering</span>
      <span class="tag-s" style="left:63px;top:180px">Roof Repair</span>
      <span class="tag-l tag-faint" style="left:102px;top:194px">Welsh Slate</span>
      <span class="tag-s" style="left:21px;top:218px">Downpipe Installation</span>
      <span class="tag-m" style="left:41px;top:231px">Quality Workmanship</span>
      <span class="tag-s" style="left:140px;top:248px">Leaking Roof</span>
      <span class="tag-m" style="left:12px;top:261px">Long Lasting Roof</span>
      <span class="tag-s" style="left:85px;top:278px">Roof Maintenance</span>
    </div>

    <footer class="site-footer">
      <span>© 2011 Tallowcrest Slate</span>
      <nav class="footer-nav">
        <span>Home</span><span>Slate Roof Repairs</span><span>Slate Reroofing</span><span>Slate Roof Benefits</span><span>Other Services</span><span>Photo Gallery</span><span>FAQs</span><span>Free Quote</span><span>Contact Us</span>
      </nav>
    </footer>
  </main>
</body>
</html>
```